Bramblewood haven a space of healing for first responders veterans and caregivers.

Build a complete website for Bramblewood Haven, a wellness and retreat company focused on first responders, caregivers, veterans, and individuals navigating PTSD, depression, anxiety, and burnout.

Style & Branding:

Blend American pride (strong, grounded, resilient) with feminine & masculine balance (warmth, nurturing, strength).

Incorporate imagery of fire, light, and renewal (aligned with Bramblewood Haven’ logo and flame theme).

Use colors that reflect trust, healing, and vitality: deep blues/greens for calm, earthy tones for grounding, fire-inspired accents (gold/orange/red) for resilience.

Clean, modern layout that feels sacred yet professional, approachable but inspiring.

Homepage:

Hero section with a bold headline: “Bramblewood Haven – Calm and Courage for Daily Guardians”.

Background image: people gathered around a retreat fire circle or blended visuals of first responders & nature.

Call-to-Action buttons:

“Book a Steady Roots Mapping Session” (Calendly integration).

“Take the Free Steady Roots Checkup” (Jotform or embedded form).

Features & Pages:

Upcoming Retreats Page

Pull in graphics/photos from current website or provided assets.

Highlight retreat details: dates, location, themes (somatics, yoga, breathwork, psychedelic integration, resilience training).

Easy booking option (linked to Calendly or built-in checkout).

Programs & Coaching

Steady Roots Mapping Session booking (Calendly).

Coaching services (mental health, somatic healing, integrative practices).

Workshop offers for businesses/organizations to increase productivity and resilience.

Free Resource Lead Magnet

“Take the Steady Roots Checkup” → Auto-email delivery of free Grounded Body Guide (PDF).

Clear funnel integration: quiz → email capture → deliver PDF → upsell to retreats or calls.

About Page

Founder bio: Corinne Halvorsen – Retired firefighter (14 years), trauma-informed resiliency coach, founder of Bramblewood Haven. Speaker kit included for reference of get to know mr and the subjects i speak on professionally as a paid speaker.

Story of transformation from PTSD and frontline burnout → mission to help others heal.

Healing Modalities Page

Somatics, yoga, breathwork, psychedelic-assisted healing, integrative retreats.

Explain how these practices restore nervous system balance, resilience, and purpose.

Contact Page

Direct email & phone.

Embedded chat option if available.

Functionality:

Calendly integration for retreat calls, coaching sessions, and workshops.

E-commerce capability to sell books, PDFs, and courses (Coursebox or integrated Shopify/Stripe).

SEO optimized with keywords: PTSD healing retreats, resilience coaching, somatics workshops, nervous system reset, first responder retreats, caregiver healing, veteran wellness.

Mobile-optimized for easy scheduling and access.

Tone & Messaging:

Empathetic, authentic, and encouraging.

Balance between professional mental health support and personal lived experience.

Messaging to emphasize: “You are not alone. Healing is possible. Rekindle your strength and resilience.”

men and women on the frontlines caregivers veterans first responders

wellness, first responders

1 page

• first responder blend with holistic nature relaxation vibes. clear link to jotform quiz, calendly book your custom blue print phone call
• integrated about me and my business partner page messaging around psylocibin mdma medicine journies such as Quiet Harbor Gathering Open Meadow Gathering Tending the Roots Deepening Stillness Gathering The Slow Tide River Stone Return
• mention of psilocybin directly, mention licensed therapist or other licensing

```html
<!DOCTYPE html>
<html lang="en">
<head>
<meta charset="utf-8">
<title>Bramblewood Haven – Calm and Courage for Daily Guardians</title>
<link href="https://fonts.googleapis.com/css2?family=Montserrat:wght@400;500;600;700;800&family=Inter:wght@400;500;600&display=swap" rel="stylesheet">
<style>
:root{
  --crimson:#a51f2b;
  --crimson-dark:#8c1722;
  --orange:#e0582a;
  --amber:#e39a2c;
  --gold:#f0a830;
  --ink:#1d1d1d;
  --text:#2b2b2b;
  --muted:#555;
  --cream:#fbeee8;
  --white:#fff;
  --night:#0d0d0d;
  --head:'Montserrat',sans-serif;
  --body:'Inter',sans-serif;
}
*{box-sizing:border-box;margin:0;padding:0}
html,body{width:1200px;height:5059px;overflow:hidden}
body{position:relative;font-family:var(--body);color:var(--text);background:var(--white)}
.abs{position:absolute}
.section{position:absolute;left:0;width:1200px}
.title{position:absolute;left:0;width:1200px;text-align:center;font-family:var(--head);font-size:46px;font-weight:400;letter-spacing:1px;color:var(--ink)}
.title b{font-weight:800;color:var(--orange)}
.title.light{color:var(--white)}
.title.light b{color:var(--white)}
.title-rule{position:absolute;left:570px;width:60px;height:4px;background:var(--orange);border-radius:2px}
.light-rule{background:var(--white)}
.btn{position:absolute;display:inline-flex;align-items:center;gap:8px;font-family:var(--head);font-weight:700;font-size:15px;color:var(--white);border-radius:30px;text-transform:uppercase;padding:0 26px}
.flame{width:18px;height:22px}

/* hero */
.hero{top:0;height:720px;background:radial-gradient(ellipse at 70% 45%,#e8741e 0%,#b23c12 28%,#3a1a10 60%,#141010 100%)}
.hero-photo{position:absolute;inset:0}
.logo-badge{position:absolute;width:112px;height:112px;border-radius:50%;background:var(--crimson);display:flex;align-items:center;justify-content:center;text-align:center;font-family:var(--head);font-weight:700;color:var(--white);font-size:12px;line-height:1.3;letter-spacing:.5px}
.topbar{position:absolute;top:18px;right:110px;display:flex;gap:34px;font-family:var(--head);font-size:14px;font-weight:500;color:var(--white)}
.topbar span{display:flex;align-items:center;gap:10px}
.ic-dot{width:24px;height:24px;border-radius:50%;background:var(--amber);display:inline-flex;align-items:center;justify-content:center}
.nav{position:absolute;top:76px;left:340px;display:flex;gap:40px;font-family:var(--head);font-size:13px;font-weight:500;color:var(--white)}
.nav .active{position:relative}
.nav .active:before{content:"";position:absolute;top:-20px;left:0;width:100%;height:2px;background:var(--amber)}
.quote-btn{position:absolute;top:68px;left:958px;height:32px;padding:0 18px;border-radius:18px;background:var(--orange);color:var(--white);font-family:var(--head);font-weight:700;font-size:12px;display:flex;align-items:center}
.hero h1{position:absolute;top:218px;left:107px;font-family:var(--head);color:var(--white);font-weight:800;text-transform:uppercase;line-height:1.18;font-size:44px;letter-spacing:.5px}
.hero h1 .big{font-size:62px;display:block;line-height:1.05}
.hero .btn{height:50px;font-size:15px}

/* expect */
.expect{top:680px;height:520px}
.card-x{position:absolute;top:228px;width:214px;height:176px;background:var(--white);border-radius:8px;text-align:center;font-family:var(--head);font-weight:500;font-size:17px;color:var(--ink);line-height:1.5;padding-top:36px}
.card-x svg{display:block;margin:0 auto 12px}
.card-x.focus{top:205px;height:222px;width:238px;background:linear-gradient(#d98a1f,#c87515);border:2px solid #f6c77a;color:var(--white);padding:20px 18px 0}
.card-x.focus h3{font-size:16px;font-weight:600;margin:4px 0 8px}
.card-x.focus p{font-family:var(--body);font-size:11.5px;font-weight:600;line-height:1.6}

/* founder */
.founder{top:1200px;height:790px}
.photo-ring{position:absolute;border-radius:50%}
.founder-text{position:absolute;left:662px;top:206px;width:446px}
.name-title{font-family:var(--head);font-weight:700;font-size:30px;color:var(--orange);line-height:1.3}
.bio{font-size:16px;line-height:1.85;color:var(--text);text-align:justify}
.bio-small{font-size:14px;line-height:2;color:var(--muted);text-align:justify}
.read-btn{height:52px;background:var(--crimson)}

/* coaching */
.coaching{top:1990px;height:660px}
.service{position:absolute;border-radius:50%;overflow:hidden;border:6px solid var(--white)}
.service .label{position:absolute;left:0;right:0;bottom:0;text-align:center;font-family:var(--head);font-weight:500;color:var(--ink)}

/* team */
.partner{top:2650px;height:760px}
.partner-text{position:absolute;left:110px;top:180px;width:446px}

/* offer */
.offer{top:3410px;height:520px;background:var(--cream)}
.offer-card{position:absolute;top:195px;width:275px;height:242px;background:var(--white);border-radius:8px;box-shadow:0 4px 18px rgba(0,0,0,.1);text-align:center;padding:28px 22px 0}
.offer-card h3{font-family:var(--head);font-weight:600;font-size:17px;color:var(--ink);margin:14px 0 12px}
.offer-card p{font-size:12.5px;line-height:1.8;color:var(--muted)}

/* resources */
.resources{top:3900px;height:740px}
.res-card{position:absolute;top:240px;width:293px;height:316px;background:var(--white);border-radius:10px;padding:14px;text-align:center}
.res-img{height:206px;border-radius:8px}
.res-card h3{font-family:var(--head);font-weight:700;font-size:20px;color:var(--ink);margin-top:16px}
.stars{color:var(--orange);font-size:14px;letter-spacing:2px;margin-top:4px}
.arrow-c{position:absolute;top:4282px;width:34px;height:34px;border-radius:50%;border:2px solid var(--white);display:flex;align-items:center;justify-content:center}

/* footer */
.footer{top:4630px;height:429px;background:var(--night);color:var(--white)}
.foot-col{position:absolute;top:110px}
.foot-col h4{font-family:var(--head);font-weight:500;font-size:18px;letter-spacing:.5px;margin-bottom:20px}
.foot-col li{list-style:none;font-size:14px;margin-bottom:16px;display:flex;align-items:center;gap:10px}
.contact-row{display:flex;gap:14px;align-items:flex-start;font-size:14px;line-height:1.9;margin-bottom:18px}
.c-ic{width:30px;height:30px;border-radius:50%;background:var(--white);flex:none;display:flex;align-items:center;justify-content:center}
.copy{position:absolute;left:110px;top:370px;font-size:14px;font-weight:600}
.socials{position:absolute;top:362px;left:930px;display:flex;gap:18px}
.socials span{width:26px;height:26px;border-radius:50%;border:2px solid var(--white)}
</style>
</head>
<body>

<!-- HERO -->
<header class="section hero">
  <div class="hero-photo" role="img" aria-label="Firefighter in protective gear kneeling before a wall of fire and smoke"></div>
  <div class="logo-badge" style="left:113px;top:8px">BRAMBLEWOOD<br>HAVEN</div>
  <div class="topbar">
    <span><i class="ic-dot"><svg width="12" height="12" viewBox="0 0 24 24"><path fill="#fff" d="M6.6 10.8a15 15 0 0 0 6.6 6.6l2.2-2.2c.3-.3.7-.4 1-.2 1.1.4 2.3.6 3.6.6.6 0 1 .4 1 1V20c0 .6-.4 1-1 1A17 17 0 0 1 3 4c0-.6.4-1 1-1h3.5c.6 0 1 .4 1 1 0 1.3.2 2.5.6 3.6.1.3 0 .7-.2 1z"/></svg></i>Call +1-555-214-7730</span>
    <span><i class="ic-dot"><svg width="12" height="12" viewBox="0 0 24 24"><path fill="#fff" d="M3 5h18v14H3z M3 5l9 7 9-7" stroke="#e39a2c" stroke-width="1.5"/></svg></i>hello@bramblewoodhaven.com</span>
  </div>
  <nav class="nav">
    <span class="active">HOME</span><span>ABOUT</span><span>COACHING SERVICE</span><span>COURSES</span><span>CONTACT US</span>
  </nav>
  <div class="quote-btn">GET A QUOTE</div>
  <h1><span class="big">Bramblewood</span>Haven – Calm and<br>Courage for Daily<br>Guardians</h1>
  <a class="btn" style="left:110px;top:473px;background:var(--orange)">Book a Steady Roots Mapping Session</a>
  <a class="btn" style="left:110px;top:540px;background:var(--amber)">Take the Free Steady Roots Checkup</a>
</header>

<!-- WHAT TO EXPECT -->
<section class="section expect">
  <svg class="abs" style="left:0;top:0" width="1200" height="520" viewBox="0 0 1200 520" preserveAspectRatio="none">
    <path fill="#a51f2b" d="M0 30 C120 10 220 40 330 28 C450 15 520 50 600 30 C700 5 800 40 900 30 C1000 20 1100 10 1200 20 L1200 470 C1100 480 1000 500 900 495 C780 488 700 510 600 505 C480 498 380 480 260 495 C160 505 80 490 0 480 Z"/>
  </svg>
  <svg class="abs" style="left:582px;top:-28px" width="36" height="52" viewBox="0 0 36 52"><path fill="#fff" d="M18 2C22 14 34 22 32 36 30 46 24 50 18 50 10 50 4 44 4 36 4 26 14 22 18 2Z"/></svg>
  <h2 class="title light" style="top:92px">WHAT TO <b>EXPECT</b></h2>
  <div class="title-rule light-rule" style="top:165px"></div>

  <div class="card-x" style="left:112px">
    <svg width="60" height="46" viewBox="0 0 60 46"><rect x="14" y="4" width="34" height="24" rx="3" fill="none" stroke="#e0582a" stroke-width="3"/><circle cx="16" cy="30" r="6" fill="#e0582a"/><rect x="6" y="36" width="24" height="8" rx="3" fill="#e0582a"/><path d="M34 12h10M34 18h8" stroke="#e0582a" stroke-width="3"/></svg>
    Weekly<br>Live Sessions
  </div>
  <div class="card-x focus" style="left:354px">
    <svg width="46" height="46" viewBox="0 0 46 46"><circle cx="23" cy="23" r="20" fill="none" stroke="#fff" stroke-width="3"/><circle cx="23" cy="16" r="5" fill="#fff"/><path d="M13 32c3-7 17-7 20 0" fill="#fff"/></svg>
    <h3>Daily Somatic Practices</h3>
    <p>Daily somatic practices promote embodiment and personal growth, helping participants integrate learning into their lives.</p>
  </div>
  <div class="card-x" style="left:620px">
    <svg width="40" height="46" viewBox="0 0 40 46"><ellipse cx="20" cy="21" rx="13" ry="18" fill="none" stroke="#e0582a" stroke-width="3"/><path d="M14 40h12" stroke="#e0582a" stroke-width="3"/><path d="M14 18l6-6 6 6" fill="none" stroke="#e0582a" stroke-width="2"/></svg>
    Personalized<br>Self-Reflection Tools
  </div>
  <div class="card-x" style="left:875px">
    <svg width="56" height="46" viewBox="0 0 56 46"><circle cx="28" cy="10" r="6" fill="#e0582a"/><circle cx="12" cy="18" r="5" fill="#e0582a"/><circle cx="44" cy="18" r="5" fill="#e0582a"/><path d="M6 44l10-18 12 10 12-10 10 18" fill="none" stroke="#e0582a" stroke-width="4"/></svg>
    Supportive<br>Group Environment
  </div>
</section>

<!-- FOUNDER -->
<section class="section founder">
  <h2 class="title" style="top:70px"><b>MEET OUR</b> FOUNDER</h2>
  <div class="title-rule" style="top:148px"></div>
  <div class="photo-ring" style="left:97px;top:200px;width:493px;height:480px;background:var(--crimson)"></div>
  <div class="photo-ring" style="left:107px;top:204px;width:480px;height:470px;background:linear-gradient(135deg,#6b4a3a,#b8a48a 45%,#3a3a48)" role="img" aria-label="Founder in firefighter turnout gear and helmet beside a fire engine"></div>
  <div class="logo-badge" style="left:456px;top:540px;width:150px;height:150px;border:6px solid #fff;font-size:15px">BRAMBLEWOOD<br>HAVEN</div>
  <div class="founder-text">
    <div class="name-title">Hii, I’m Corinne Halvorsen</div>
    <p class="bio" style="margin-top:6px">Retired firefighter (14 years), trauma-informed resiliency coach, founder of Bramblewood Haven. Speaker kit included for reference of get to know mr and the subjects i speak on professionally as a paid speaker.</p>
    <p class="bio-small" style="margin-top:52px">We are a trauma-informed wellness company dedicated to helping individuals recover from burnout, trauma, and major life transitions. Our immersive retreats, workshops, and one-on-one coaching are designed to guide you back to a place of grounding, self-reconnection, clarity, and purpose.</p>
  </div>
  <a class="btn read-btn" style="left:662px;top:612px"><svg class="flame" viewBox="0 0 36 52"><path fill="#fff" d="M18 2C22 14 34 22 32 36 30 46 24 50 18 50 10 50 4 44 4 36 4 26 14 22 18 2Z"/></svg>Read More</a>
</section>

<!-- COACHING SERVICES -->
<section class="section coaching">
  <div class="abs" style="left:0;top:0;width:1200px;height:375px;background:linear-gradient(90deg,#e0582a,#e8903a 50%,#d9602a)" role="img" aria-label="Warm orange wash over a photo of a calm support gathering"></div>
  <div class="abs" style="left:0;top:235px;width:1200px;height:140px;background:var(--crimson)"></div>
  <svg class="abs" style="left:0;top:0" width="1200" height="110" viewBox="0 0 1200 110"><path fill="#e39a2c" d="M0 0h1200v60C900 90 700 30 600 80 480 30 300 100 0 70Z"/></svg>
  <h2 class="title light" style="top:80px"><b>COACHING</b> SERVICES</h2>
  <div class="title-rule light-rule" style="top:152px"></div>

  <div class="service" style="left:110px;top:260px;width:305px;height:305px;background:linear-gradient(135deg,#5a4a40,#c69a5a)" role="img" aria-label="Small group talking together in a supportive circle">
    <div class="label" style="height:100px;background:var(--amber);font-size:19px;padding-top:30px">Mental Health</div>
  </div>
  <div class="service" style="left:788px;top:260px;width:305px;height:305px;background:linear-gradient(135deg,#4a6a40,#d8b080)" role="img" aria-label="Hands placing fine acupuncture needles on a back">
    <div class="label" style="height:100px;background:var(--amber);font-size:19px;padding-top:22px;line-height:1.15">Integrative<br>practices</div>
  </div>
  <div class="service" style="left:388px;top:200px;width:430px;height:430px;background:linear-gradient(135deg,#7a5a48,#c99a7a 55%,#4a4a48)" role="img" aria-label="Person receiving a calming hot stone treatment">
    <div class="label" style="height:130px;background:var(--orange);font-size:22px;padding-top:26px">
      <svg width="38" height="32" viewBox="0 0 38 32"><path fill="#1d1d1d" d="M19 6c5 6 5 14 0 20-5-6-5-14 0-20ZM4 14c7 0 12 5 14 12-8 0-13-5-14-12ZM34 14c-1 7-6 12-14 12 2-7 7-12 14-12Z"/></svg><br>Somatic Healing
    </div>
  </div>
</section>

<!-- PARTNER -->
<section class="section partner">
  <h2 class="title" style="top:42px"><b>MEET</b> DELIA MARCHETTI</h2>
  <div class="title-rule" style="top:118px"></div>
  <div class="partner-text">
    <div class="name-title" style="text-align:justify">Hii, I’m Delia Marchetti, Facilitator and Partner</div>
    <p class="bio" style="margin-top:8px">Delia Marchetti is a vital part of the Bramblewood Haven team, bringing a wealth of knowledge and compassionate experience to our programs. With certifications as a Holistic Health &amp; Wellness Practitioner, Healing Arts Facilitator, Grief Recovery Specialist, Spiritual Healing Guide, and Death &amp; Transitions Coach, Delia offers a deeply integrative approach to wellness.</p>
    <p class="bio-small" style="margin-top:36px">As a retired Firefighter/Paramedic, she understands the unique challenges faced by first responders and serves as a dedicated Mental Wellness Advocate within that community.</p>
  </div>
  <a class="btn read-btn" style="left:110px;top:610px"><svg class="flame" viewBox="0 0 36 52"><path fill="#fff" d="M18 2C22 14 34 22 32 36 30 46 24 50 18 50 10 50 4 44 4 36 4 26 14 22 18 2Z"/></svg>Read More</a>
  <div class="photo-ring" style="left:612px;top:160px;width:496px;height:496px;background:linear-gradient(var(--amber),var(--crimson))"></div>
  <div class="photo-ring" style="left:622px;top:170px;width:476px;height:476px;background:linear-gradient(135deg,#4a3a30,#a88a70 50%,#2e6a6a)" role="img" aria-label="Portrait of the facilitator and partner"></div>
</section>

<!-- WE OFFER -->
<section class="section offer">
  <h2 class="title" style="top:70px"><b>WE</b> OFFER</h2>
  <div class="title-rule" style="top:140px"></div>
  <div class="offer-card" style="left:110px">
    <svg width="60" height="60" viewBox="0 0 60 60"><circle cx="30" cy="14" r="8" fill="none" stroke="#e0582a" stroke-width="3"/><path d="M12 50c2-14 34-14 36 0M6 54h48" fill="none" stroke="#e0582a" stroke-width="3"/></svg>
    <h3>Retreats &amp; Workshops</h3>
    <p>Transformative group experiences designed for healing, growth, and connection in safe and supportive environments.</p>
  </div>
  <div class="offer-card" style="left:462px">
    <svg width="70" height="60" viewBox="0 0 70 60"><rect x="10" y="4" width="50" height="28" rx="3" fill="#e0582a"/><path d="M16 12h38M16 20h26" stroke="#fff" stroke-width="3"/><circle cx="14" cy="42" r="6" fill="#e0582a"/><circle cx="35" cy="42" r="6" fill="#e0582a"/><circle cx="56" cy="42" r="6" fill="#e0582a"/><path d="M4 58c2-8 18-8 20 0M25 58c2-8 18-8 20 0M46 58c2-8 18-8 20 0" fill="#e0582a"/></svg>
    <h3>One-on-One Coaching</h3>
    <p>Personalized coaching sessions tailored to your journey, helping you gain clarity, resilience, and alignment in life.</p>
  </div>
  <div class="offer-card" style="left:813px">
    <svg width="60" height="60" viewBox="0 0 60 60"><path d="M10 22a12 10 0 0 1 24 0Z" fill="#e0582a"/><path d="M30 16a12 10 0 0 1 24 0Z" fill="#e39a2c"/><path d="M22 22v34M42 16v40M14 56h34" stroke="#e0582a" stroke-width="3"/></svg>
    <h3>Psychedelic Integration</h3>
    <p>Guidance and support to process and integrate psychedelic experiences into lasting positive change.</p>
  </div>
</section>

<!-- RESOURCES -->
<section class="section resources">
  <svg class="abs" style="left:0;top:0" width="1200" height="740" viewBox="0 0 1200 740" preserveAspectRatio="none">
    <defs><linearGradient id="resGrad" x1="0" y1="0" x2="1" y2="1"><stop offset="0" stop-color="#e39a2c"/><stop offset=".5" stop-color="#e07d28"/><stop offset="1" stop-color="#e39a2c"/></linearGradient></defs>
    <path fill="url(#resGrad)" d="M0 20C150 0 260 40 400 25 560 8 700 40 850 22 1000 5 1100 30 1200 15V740H0Z"/>
  </svg>
  <div class="abs" style="left:0;top:20px;width:1200px;height:720px" role="img" aria-label="Faint background of folded firefighter turnout gear"></div>
  <h2 class="title light" style="top:140px"><b>EXPLORE</b> RESOURCES</h2>
  <div class="title-rule light-rule" style="top:212px"></div>
  <div class="res-card" style="left:112px">
    <div class="res-img" style="background:linear-gradient(#f4f4f4,#dfe7ec)" role="img" aria-label="Grounded Body Guide book cover"></div>
    <h3>BOOKS</h3><div class="stars">★★★★★</div>
  </div>
  <div class="res-card" style="left:455px">
    <div class="res-img" style="background:linear-gradient(135deg,#3a4a5a,#8a9aa8)" role="img" aria-label="Smiling learner working on a laptop"></div>
    <h3>COURSES</h3><div class="stars">★★★★★</div>
  </div>
  <div class="res-card" style="left:796px">
    <div class="res-img" style="background:linear-gradient(135deg,#1a2a3a,#4a6a8a)" role="img" aria-label="Digital PDF document on a screen"></div>
    <h3>PDFs</h3><div class="stars">★★★★★</div>
  </div>
  <a class="btn read-btn" style="left:515px;top:622px;height:52px"><svg class="flame" viewBox="0 0 36 52"><path fill="#fff" d="M18 2C22 14 34 22 32 36 30 46 24 50 18 50 10 50 4 44 4 36 4 26 14 22 18 2Z"/></svg>Shop Now</a>
</section>
<div class="arrow-c" style="left:35px"><svg width="14" height="14" viewBox="0 0 14 14"><path d="M12 7H2M6 3L2 7l4 4" fill="none" stroke="#fff" stroke-width="2"/></svg></div>
<div class="arrow-c" style="left:1131px"><svg width="14" height="14" viewBox="0 0 14 14"><path d="M2 7h10M8 3l4 4-4 4" fill="none" stroke="#fff" stroke-width="2"/></svg></div>

<!-- FOOTER -->
<footer class="section footer">
  <div class="logo-badge" style="left:138px;top:125px;width:170px;height:170px;font-size:17px">BRAMBLEWOOD<br>HAVEN</div>
  <div class="foot-col" style="left:387px">
    <h4>QUICK LINKS</h4>
    <ul><li>➜ Home</li><li>➜ About</li><li>➜ Services</li><li>➜ Courses</li><li>➜ Contact Us</li></ul>
  </div>
  <div class="foot-col" style="left:613px">
    <h4>HELP LINKS</h4>
    <ul><li>➜ FAQ</li><li>➜ Terms of use</li><li>➜ Privacy Policy</li><li>➜ Support Links</li><li>➜ Conditions</li></ul>
  </div>
  <div class="foot-col" style="left:842px">
    <h4>CONTACT US</h4>
    <div class="contact-row"><span class="c-ic"><svg width="14" height="16" viewBox="0 0 14 18"><path fill="#0d0d0d" d="M7 0a7 7 0 0 1 7 7c0 5-7 11-7 11S0 12 0 7a7 7 0 0 1 7-7Zm0 4a3 3 0 1 0 0 6 3 3 0 0 0 0-6Z"/></svg></span><span>Bramblewood Haven<br>United States</span></div>
    <div class="contact-row"><span class="c-ic"><svg width="14" height="14" viewBox="0 0 24 24"><path fill="#0d0d0d" d="M6.6 10.8a15 15 0 0 0 6.6 6.6l2.2-2.2c.3-.3.7-.4 1-.2 1.1.4 2.3.6 3.6.6.6 0 1 .4 1 1V20c0 .6-.4 1-1 1A17 17 0 0 1 3 4c0-.6.4-1 1-1h3.5c.6 0 1 .4 1 1 0 1.3.2 2.5.6 3.6.1.3 0 .7-.2 1z"/></svg></span><span style="padding-top:4px">+1 555 214 7730</span></div>
    <div class="contact-row"><span class="c-ic"><svg width="14" height="12" viewBox="0 0 24 18"><path d="M1 1h22v16H1zM1 1l11 8 11-8" fill="none" stroke="#0d0d0d" stroke-width="2"/></svg></span><span style="padding-top:4px">hello@bramblewoodhaven.com</span></div>
  </div>
  <div class="abs" style="left:110px;top:350px;width:980px;height:1px;background:#333"></div>
  <div class="copy">Copyrights@2025.Bramblewood Haven.All Rights Reserved</div>
  <div class="socials"><span></span><span></span><span></span><span></span></div>
</footer>

</body>
</html>
```